Webdesign für Herstellung von Geschenk- und Dekorationsartikeln
Kobalt Prismo ist ein sehr angenehmer und professioneller Designer, der sich viele Gedanken über mein Projekt gemacht hat und ein Design, passend zu meinen Artikeln entworfen hat. Neben einer kompetenten Beratung gab es viele hilfreiche Vorschläge, die über den eigentlichen Auftrag hinaus gingen. Der Designer ist sehr zu empfehlen. Vielen Dank für den freundlichen Kontakt!
Zielgruppe
Wir sind eine kleine Firma, die mit einem Lasergravierer Geschenk- und Dekorationsartikel herstellt, verziert und beschriftet. Hierzu wird hauptsächlich Holz, Papier, Kork, Filz und Glas als Material eingesetzt.
Auch Schmuck , wie z.B. Kettenanhänger und Ohrringe aus Holz werden gefertigt.
Außerdem werden Fotogravur-Arbeiten nach Kundenwunsch angeboten.
Haupt-Zielgruppe sind Frauen ab 30.
Aufgabenstellung
Das Design soll etwas verspielt sein und Freude an den kleinen Dingen des Lebens ausdrücken. Es soll nicht zu sachlich und kühl sein.
Das vorhandene Logo wird bereit gestellt.
Es existiert noch keine Webseite. Die zukünftige Webseite soll über einen Shop verfügen.
Von der Shop-Darstellung her, hat mir die Webseite 'www.qvhauswerk.ch' gefallen.
Es wäre gut, wenn die im Logo vorhandenen Farben auch auf dem Design für die Webseite auftauchen würden.
Als Design-Tool wäre Adobe Photoshop (PSD) für die Erstellung gut.

```html
<!DOCTYPE html>
<html lang="de">
<head>
<meta charset="utf-8">
<title>Lindora – Holzcraft Ketten</title>
<link rel="stylesheet" href="https://fonts.googleapis.com/css2?family=Cabin:wght@400;500;600;700&display=swap">
<style>
  :root{
    --cream:#f1e8df;
    --cream-deep:#e9dfd5;
    --gold:#b5853f;
    --gold-soft:#c9a26a;
    --ink:#6b6b6b;
    --logo-ink:#6e6e6e;
    --white:#ffffff;
  }
  *{margin:0;padding:0;box-sizing:border-box}
  html,body{width:924px;height:1200px;overflow:hidden;background:var(--white)}
  body{font-family:"Cabin",sans-serif;color:var(--gold);position:relative}
  .backdrop{position:absolute;left:0;top:0;width:924px;height:800px}
  .abs{position:absolute}
  .brand{display:flex;align-items:center;gap:8px;color:var(--logo-ink);font-weight:500}
  .brand-dot{width:14px;height:14px;border-radius:50%;background:var(--gold)}
  .header-brand{left:104px;top:58px;font-size:30px}
  .nav{top:66px;left:397px;display:flex;font-size:10px;letter-spacing:.4px;font-weight:500}
  .nav a{color:var(--gold);text-decoration:none;position:absolute;white-space:nowrap}
  .icons{top:64px;left:752px}
  .kicker{left:126px;top:180px;border-left:2px solid var(--gold);padding-left:5px;font-size:8.5px;font-weight:600;line-height:10px}
  .hero-title{left:140px;top:262px;font-size:30px;font-weight:700;line-height:38px;letter-spacing:.5px}
  .hero-sub{left:145px;top:341px;font-size:8.5px;font-weight:600}
  .btn-primary{left:146px;top:364px;width:98px;height:26px;border-radius:13px;background:var(--gold);color:var(--white);font-size:9.5px;font-weight:500;display:flex;align-items:center;justify-content:center;box-shadow:2px 2px 3px rgba(0,0,0,.15)}
  .dot{left:100px;width:11px;height:11px;border-radius:50%;border:1px solid var(--gold)}
  .dot.is-active::after{content:"";position:absolute;left:2px;top:2px;width:5px;height:5px;border-radius:50%;background:var(--gold)}
  .hero-frame{left:455px;top:170px;width:274px;height:274px;border-radius:50%;background:var(--cream-deep)}
  .hero-photo{left:467px;top:183px;width:250px;height:250px;border-radius:50%;background:radial-gradient(circle at 45% 45%,#c9a64a,#b38e32 70%,#a07c2a)}
  .scroll-track{left:826px;top:287px;width:2px;height:166px;background:#e4d3c1}
  .scroll-thumb{left:824px;top:287px;width:5px;height:31px;background:var(--gold)}
  .section-title{left:0;width:938px;top:590px;text-align:center;font-size:15px;font-weight:600}
  .section-title span{border-bottom:1px solid var(--gold-soft);padding-bottom:1px}
  .card{top:661px;width:187px}
  .card-photo{width:187px;height:187px}
  .card-name{font-size:10px;margin-top:8px;white-space:nowrap}
  .card-text{font-size:7.8px;color:var(--ink);line-height:10px;margin-top:2px}
  .card-price{font-size:10.5px;font-weight:700;margin-top:10px}
  .arrow{top:746px}
  .btn-outline{left:410px;top:932px;width:119px;height:25px;border:1px solid var(--gold);border-radius:3px;font-size:9px;font-weight:600;letter-spacing:.4px;display:flex;align-items:center;justify-content:center}
  .footer-brand{left:104px;top:1038px;font-size:24px}
  .foot-head{font-size:7px;font-weight:700;letter-spacing:.3px}
  .foot-links{font-size:6px;line-height:7.6px;list-style:none}
  .social{top:1024px;left:762px;display:flex;gap:9px}
  .social span{width:8px;height:8px;border-radius:50%;background:var(--gold)}
</style>
</head>
<body>
  <svg class="backdrop" viewBox="0 0 924 800" aria-hidden="true">
    <path d="M0 0H924V711C720 752 330 720 0 523Z" fill="var(--cream)"/>
  </svg>

  <header>
    <div class="abs brand header-brand"><span class="brand-dot"></span>Lindora</div>
    <nav class="abs nav">
      <a style="left:0">HOME</a>
      <a style="left:49px">ÜBER UNS</a>
      <a style="left:122px">PRODUKTE</a>
      <a style="left:201px">BLOG</a>
      <a style="left:253px">KONTAKT</a>
    </nav>
    <svg class="abs icons" width="80" height="16" viewBox="0 0 80 16" aria-hidden="true" fill="none" stroke="var(--gold)" stroke-width="1.6">
      <circle cx="6" cy="6" r="4.2" stroke-width="2"/><path d="M9 9l4 4" stroke-width="2.4" stroke-linecap="round"/>
      <circle cx="34" cy="5" r="3"/><path d="M28.5 14c0-3.5 2.5-5 5.5-5s5.5 1.5 5.5 5z"/>
      <path d="M55 2h2.5l2 8h8l1.5-6h-10.5"/><circle cx="60" cy="13" r="1.2"/><circle cx="66.5" cy="13" r="1.2"/>
    </svg>
  </header>

  <section class="hero">
    <div class="abs kicker">Sommer Kollektion<br>Ketten</div>
    <h1 class="abs hero-title">Holzcraft<br>Ketten</h1>
    <p class="abs hero-sub">Individualisierte Ketten aus Holz</p>
    <div class="abs btn-primary">zum Produkt</div>
    <span class="abs dot is-active" style="top:296px"></span>
    <span class="abs dot" style="top:319px"></span>
    <span class="abs dot" style="top:341px"></span>
    <div class="abs hero-frame"></div>
    <div class="abs hero-photo" role="img" aria-label="Foto eines rautenförmigen Holzanhängers an einer Lederkette auf senfgelbem Stoff"></div>
    <div class="abs scroll-track"></div>
    <div class="abs scroll-thumb"></div>
  </section>

  <section class="new-products">
    <h2 class="abs section-title"><span>Neu im Sortiment</span></h2>
    <svg class="abs arrow" style="left:90px" width="16" height="14" viewBox="0 0 16 14" aria-hidden="true"><path d="M15 7H2M7 1.5L1.5 7 7 12.5" fill="none" stroke="var(--gold)" stroke-width="2.2"/></svg>
    <svg class="abs arrow" style="left:814px" width="16" height="14" viewBox="0 0 16 14" aria-hidden="true"><path d="M1 7h13M9 1.5L14.5 7 9 12.5" fill="none" stroke="var(--gold)" stroke-width="2.2"/></svg>

    <article class="abs card" style="left:162px">
      <div class="card-photo" role="img" aria-label="Foto eines gerahmten Spruchbildes mit weißer Schrift auf grauem Grund" style="background:linear-gradient(135deg,#d9d4d2,#a3a4a8 50%,#c7c2c0)"></div>
      <h3 class="card-name">Personalisierte Bilder</h3>
      <p class="card-text">personalisierte Bilder als Geschenk zum Geburtstag ihrer Freunde</p>
      <p class="card-price">3.33€</p>
    </article>
    <article class="abs card" style="left:377px">
      <div class="card-photo" role="img" aria-label="Foto eines gravierten Korkuntersetzers mit Spruch" style="background:radial-gradient(circle,#a77b58,#8f6647 75%,#f4f0ec 78%)"></div>
      <h3 class="card-name">Personalisierte Untersetzer</h3>
      <p class="card-text">personalisierte Untersetzer als Geschenk zum Geburtstag ihrer Freunde</p>
      <p class="card-price">3.33€</p>
    </article>
    <article class="abs card" style="left:592px">
      <div class="card-photo" role="img" aria-label="Foto eines Holzbrettchens mit eingravierter Comicfigur" style="background:linear-gradient(160deg,#d8cfc4,#c4b7a8 60%,#b99d78)"></div>
      <h3 class="card-name">Personalisierte Frühstücksbrettchen</h3>
      <p class="card-text">personalisierte Frühstücksbrettchen als Geschenk zum Geburtstag ihrer Freunde</p>
      <p class="card-price">3.33€</p>
    </article>

    <div class="abs btn-outline">ALLE ANZEIGEN</div>
  </section>

  <footer>
    <div class="abs brand footer-brand"><span class="brand-dot"></span>Lindora</div>
    <p class="abs foot-head" style="left:274px;top:1023px">SITEMAP</p>
    <ul class="abs foot-links" style="left:318px;top:1024px">
      <li>Kontakt</li><li>Über Uns</li><li>Verpackung &amp; Versand</li><li>FAQ</li><li>Rücksendungen</li><li>Produkte</li>
    </ul>
    <p class="abs foot-head" style="left:421px;top:1023px">INFORMATIONEN</p>
    <ul class="abs foot-links" style="left:493px;top:1024px">
      <li>AGB</li><li>Datenschutz</li><li>Impressum</li>
    </ul>
    <div class="abs social" aria-label="Soziale Netzwerke"><span></span><span></span><span></span></div>
  </footer>
</body>
</html>
```